Small property developments

I'm just starting out developing duplex homes on urban infill sites in the Tarrowdale City Council region of Brisbane. I need a business card to give to planners, engineers and builders. I was thinking of a logo that showed two homes under a single roof which is what a duplex is, but all good development and construction themes considered. Company name will be Marty Lunde Developments.

```html
<!DOCTYPE html>
<html lang="en">
<head>
<meta charset="utf-8">
<title>Marty Lunde Developments – Business Cards</title>
<link rel="stylesheet" href="https://fonts.googleapis.com/css2?family=Bebas+Neue&family=Noto+Sans:wght@400&display=swap">
<style>
  :root {
    --stage: #5e5e5e;
    --paper: #ffffff;
    --charcoal: #3a3a3c;
    --brand-red: #d9343f;
    --ink: #3d3d3f;
    --light: #ffffff;
  }
  * { margin: 0; padding: 0; box-sizing: border-box; }
  html, body {
    width: 1200px;
    height: 758px;
    overflow: hidden;
    background: var(--stage);
  }
  .canvas {
    position: relative;
    width: 1200px;
    height: 758px;
    background: var(--stage);
  }
  .card {
    position: absolute;
    overflow: hidden;
  }
  .card--front {
    left: 348px; top: 108px;
    width: 554px; height: 242px;
    background: var(--paper);
  }
  .card--details {
    left: 120px; top: 367px;
    width: 492px; height: 284px;
    background: var(--charcoal);
  }
  .card--brand {
    left: 644px; top: 367px;
    width: 492px; height: 284px;
    background: var(--brand-red);
  }

  .wordmark {
    position: absolute;
    display: flex;
    align-items: center;
    gap: 10px;
    font-family: "Bebas Neue", sans-serif;
    font-weight: 400;
    white-space: nowrap;
    line-height: 1;
  }
  .wordmark__square {
    width: 30px;
    height: 30px;
    flex: none;
  }
  .card--front .wordmark {
    left: 34px; top: 62px;
    font-size: 40px;
    color: var(--ink);
  }
  .card--front .wordmark__square { background: var(--brand-red); }

  .card--brand .wordmark {
    left: 24px; top: 134px;
    font-size: 39px;
    color: var(--charcoal);
  }
  .card--brand .wordmark__square { background: var(--light); }

  .front-contact {
    position: absolute;
    left: 170px; top: 104px;
    width: 300px;
    text-align: center;
    font-family: "Noto Sans", sans-serif;
    font-size: 15px;
    line-height: 20px;
    color: var(--ink);
  }

  .details {
    position: absolute;
    left: 14px; top: 114px;
    font-family: "Noto Sans", sans-serif;
    color: var(--light);
  }
  .details__name {
    font-family: "Bebas Neue", sans-serif;
    font-size: 42px;
    line-height: 1;
    color: var(--light);
  }
  .details__role {
    font-size: 23px;
    line-height: 30px;
    margin-top: 2px;
  }
  .details__contact {
    margin-top: 26px;
    font-size: 25px;
    line-height: 31px;
  }
</style>
</head>
<body>
<main class="canvas">

  <section class="card card--front" aria-label="Card front">
    <div class="wordmark">
      <span class="wordmark__square"></span>
      <span class="wordmark__name">Marty Lunde Developments</span>
    </div>
    <div class="front-contact">
      <p>MARTY LUNDE | OWNER</p>
      <p>marty@lundedevelopments.au</p>
      <p>m: 043-555-0182</p>
    </div>
  </section>

  <section class="card card--details" aria-label="Contact side">
    <div class="details">
      <h1 class="details__name">Marty Lunde</h1>
      <p class="details__role">Owner</p>
      <div class="details__contact">
        <p>marty@lundedevelopments.au</p>
        <p>m: 043-555-0182</p>
      </div>
    </div>
  </section>

  <section class="card card--brand" aria-label="Brand side">
    <div class="wordmark">
      <span class="wordmark__square"></span>
      <span class="wordmark__name">Marty Lunde Developments</span>
    </div>
  </section>

</main>
</body>
</html>
```